Business Card Design

I want a simple and modern design, but also something very catching to the eye.

Also is there anyway that the text can be adjusted or changed so that I may make cards for other employees? If so, please make it so that I may edit the texts at a future date.

Reason: I need all designers to update the business card with my update information.

Industry/Entity Type

Business

Contact Information for Business Card

Owner: Marcus Velliharn
Company Name: Fun Drova
Phone # :555-273-9148
Website: fundrovaplay.com
Email: marc@fundrovaplay.com

```html
<!DOCTYPE html>
<html lang="en">
<head>
<meta charset="utf-8">
<title>Fun Drova Business Card</title>
<link rel="stylesheet" href="https://fonts.googleapis.com/css2?family=Arimo:wght@400;700&display=swap">
<style>
  :root {
    --bg: #3a3a3a;
    --card: #ffffff;
    --red: #ee2b24;
    --red-soft: #e4544b;
    --yellow: #f9d40a;
    --yellow-deep: #e2c71b;
    --blue: #1f9bd7;
    --ink: #111111;
    --muted: #9a9a9a;
  }
  * { box-sizing: border-box; margin: 0; padding: 0; }
  html, body { width: 1200px; height: 900px; overflow: hidden; }
  body {
    background: var(--bg);
    font-family: "Arimo", Arial, sans-serif;
    position: relative;
  }
  .card {
    position: absolute;
    width: 640px;
    height: 366px;
    background: var(--card);
    overflow: hidden;
    box-shadow: 0 6px 18px rgba(0,0,0,.35);
  }
  /* Front */
  .card-front { left: 60px; top: 60px; }
  .band { position: absolute; left: 0; width: 100%; background: var(--red); }
  .band-top { top: 0; height: 98px; }
  .band-bottom { bottom: 0; height: 98px; }
  .brand {
    display: flex; align-items: center; gap: 10px;
    font-weight: 700; color: var(--red); white-space: nowrap;
  }
  .brand-mark { background: var(--blue); flex: none; }
  .card-front .brand {
    position: absolute; left: 50%; top: 50%;
    transform: translate(-50%, -50%);
    font-size: 64px;
  }
  .card-front .brand-mark { width: 54px; height: 54px; }
  /* Back */
  .card-back { left: 500px; top: 474px; }
  .card-back .shapes { position: absolute; inset: 0; }
  .card-back .brand {
    position: absolute; left: 36px; top: 118px;
    font-size: 40px;
  }
  .card-back .brand-mark { width: 34px; height: 34px; }
  .person { position: absolute; left: 36px; top: 212px; }
  .person-name { color: var(--red); font-size: 25px; font-weight: 400; }
  .person-role { color: var(--muted); font-size: 12px; margin-top: 2px; }
  .contacts {
    position: absolute; left: 36px; top: 286px;
    list-style: none; font-size: 15px; color: var(--ink);
  }
  .contacts li { display: flex; align-items: center; gap: 8px; height: 21px; }
  .contact-key {
    width: 14px; height: 14px; background: var(--blue); color: #fff;
    font-size: 10px; font-weight: 700; line-height: 14px; text-align: center;
  }
</style>
</head>
<body>
  <section class="card card-front" aria-label="Card front">
    <div class="band band-top"></div>
    <div class="band band-bottom"></div>
    <div class="brand"><span class="brand-mark"></span>Fun Drova</div>
  </section>

  <section class="card card-back" aria-label="Card back">
    <svg class="shapes" viewBox="0 0 640 366" width="640" height="366" aria-hidden="true">
      <path d="M250 0 H640 V112 Q430 120 250 0 Z" fill="var(--yellow)"/>
      <path d="M470 110 Q560 118 640 112 V70 Q540 80 470 110 Z" fill="var(--yellow-deep)"/>
      <path d="M640 40 C520 66 420 200 372 366 H640 Z" fill="var(--red-soft)"/>
      <path d="M640 62 C540 92 440 220 398 366 H640 Z" fill="var(--red)"/>
    </svg>
    <div class="brand"><span class="brand-mark"></span>Fun Drova</div>
    <div class="person">
      <p class="person-name">Marcus Velliharn</p>
      <p class="person-role">Owner</p>
    </div>
    <ul class="contacts">
      <li><span class="contact-key">p</span>555-273-9148</li>
      <li><span class="contact-key">e</span>fundrovaplay.com</li>
      <li><span class="contact-key">w</span>marc@fundrovaplay.com</li>
    </ul>
  </section>
</body>
</html>
```